Ferncrest Dental, LLC business card project

Business card to be designed with current logo.
Dental office- please keep design of card that looks clean and professional.
Please include the following info:
Ferncrest Dental, LLC
Dr. Lorna Pettigrew
2871 Marlowe Street
Millbrook Vale, PA 18093
610-555-0193
ferncrestdental.office@examplemail.test
Hello everyone-
Reason: Just got back from overseas- will look at all designs and provide feedback. Thank you!
Reason: Polling my friends for the final selection-
thank you to all those that participated- so many talented designers!

```html
<!DOCTYPE html>
<html lang="en">
<head>
<meta charset="utf-8">
<title>Ferncrest Dental, LLC — Business Card</title>
<link rel="stylesheet" href="https://fonts.googleapis.com/css2?family=Open+Sans:wght@300;400&display=swap">
<style>
  :root {
    --bg-top: #ffffff;
    --bg-bottom: #c4c6c7;
    --swoosh-green: #66ff3a;
    --swoosh-edge: #d9dede;
    --brand-green: #74cf22;
    --ink: #111111;
    --brand-light: #f7f7e6;
  }
  html, body {
    margin: 0;
    padding: 0;
    overflow: hidden;
    background: #ffffff;
  }
  .card {
    position: relative;
    width: 1200px;
    height: 741px;
    overflow: hidden;
    background: linear-gradient(180deg, var(--bg-top) 0%, var(--bg-top) 22%, var(--bg-bottom) 100%);
    font-family: "Open Sans", Verdana, sans-serif;
  }
  .swoosh {
    position: absolute;
    inset: 0;
  }
  .brand {
    position: absolute;
    display: flex;
    align-items: center;
    font-weight: 300;
    white-space: nowrap;
  }
  .brand--header {
    left: 40px;
    top: 46px;
    font-size: 74px;
    color: var(--brand-green);
    letter-spacing: -1.5px;
  }
  .brand--header .brand-dot {
    width: 60px;
    height: 60px;
    margin-right: 22px;
    border-radius: 50%;
    background: var(--brand-green);
  }
  .brand--footer {
    right: 52px;
    bottom: 30px;
    font-size: 40px;
    color: var(--brand-light);
    letter-spacing: -0.5px;
  }
  .brand--footer .brand-dot {
    width: 36px;
    height: 36px;
    margin-right: 14px;
    border-radius: 50%;
    background: var(--brand-light);
  }
  .doctor-name {
    position: absolute;
    left: 68px;
    top: 238px;
    margin: 0;
    font-size: 68px;
    font-weight: 400;
    color: var(--ink);
    letter-spacing: 0.5px;
  }
  .contact-list {
    position: absolute;
    left: 102px;
    top: 342px;
    margin: 0;
    padding: 0;
    list-style: none;
    font-size: 28px;
    color: var(--ink);
    letter-spacing: 0.3px;
  }
  .contact-list li {
    display: flex;
    align-items: center;
    height: 45px;
  }
  .contact-icon {
    width: 27px;
    height: 24px;
    margin-right: 6px;
    flex: none;
  }
</style>
</head>
<body>
  <div class="card">
    <svg class="swoosh" width="1200" height="741" viewBox="0 0 1200 741" aria-hidden="true">
      <path d="M830,0 C1100,140 1085,430 700,615 C470,720 200,736 0,741" fill="none" stroke="var(--swoosh-edge)" stroke-width="12"/>
      <path d="M843,0 C1115,140 1097,430 710,613 C480,720 200,735 0,741 C500,735 1000,640 1200,430 L1200,0 Z" fill="var(--swoosh-green)"/>
    </svg>

    <div class="brand brand--header">
      <span class="brand-dot"></span>Ferncrest Dental, LLC
    </div>

    <h1 class="doctor-name">Dr. Lorna Pettigrew</h1>

    <ul class="contact-list">
      <li>
        <svg class="contact-icon" viewBox="0 0 27 24" aria-hidden="true">
          <path d="M2,12 L13.5,2 L25,12" fill="none" stroke="var(--ink)" stroke-width="2.6" stroke-linejoin="round"/>
          <path d="M6,11 V22 H21 V11" fill="none" stroke="var(--ink)" stroke-width="2.6"/>
        </svg>
        2871 Marlowe Street Millbrook Vale, PA 18093
      </li>
      <li>
        <svg class="contact-icon" viewBox="0 0 27 24" aria-hidden="true">
          <path d="M2,9 C2,4 25,4 25,9 L25,11 L19,11 L19,8 L8,8 L8,11 L2,11 Z" fill="var(--ink)"/>
          <path d="M6,12 L21,12 L24,21 L3,21 Z" fill="var(--ink)"/>
          <circle cx="13.5" cy="16" r="2.6" fill="#ffffff"/>
        </svg>
        610-555-0193
      </li>
      <li>
        <svg class="contact-icon" viewBox="0 0 27 24" aria-hidden="true">
          <rect x="3" y="5" width="21" height="15" fill="none" stroke="var(--ink)" stroke-width="1.8"/>
          <path d="M3,5 L13.5,14 L24,5 M3,20 L11,12 M24,20 L16,12" fill="none" stroke="var(--ink)" stroke-width="1.6"/>
        </svg>
        ferncrestdental.office@examplemail.test
      </li>
    </ul>

    <div class="brand brand--footer">
      <span class="brand-dot"></span>Ferncrest Dental, LLC
    </div>
  </div>
</body>
</html>
```